Resume for higher management position in a mechanical/consultant industries application*

I would like to use this resume for getting a higher position interview possibilities. My skills are multi-cultural negotiation, mechanical industry sales, outsourcing to Asia, ability to manage the agent/reseller system, well team player. multi-language Chinese/English/German specialized. Please make the design, professional, comfortable to read atmosphere.

Target Market(s)

management position, sales related

Font styles to use
Serif
Sans Serif

```html
<!DOCTYPE html>
<html lang="en">
<head>
<meta charset="utf-8">
<title>Lin-Wei Hsu – Resume</title>
<link href="https://fonts.googleapis.com/css2?family=Lato:wght@400;700&family=Fira+Sans:wght@300;400&display=swap" rel="stylesheet">
<style>
  :root {
    --ink: #333333;
    --ink-soft: #444444;
    --panel: #f0f0f0;
    --paper: #ffffff;
    --track: #eeeeee;
  }
  * { box-sizing: border-box; margin: 0; padding: 0; }
  html, body { width: 847px; height: 1200px; overflow: hidden; background: var(--paper); }
  .resume { position: relative; width: 847px; height: 1200px; font-family: "Lato", Arial, sans-serif; color: var(--ink); }

  .sidebar { position: absolute; left: 22px; top: 0; width: 391px; height: 1170px; background: var(--panel); }
  .name-bar { position: absolute; left: 38px; top: 0; width: 22px; height: 105px; background: var(--ink); }
  .name { position: absolute; left: 72px; top: 40px; font-size: 36px; font-weight: 700; color: var(--ink-soft); letter-spacing: -0.5px; }
  .role { position: absolute; left: 73px; top: 82px; font-size: 20px; letter-spacing: 4.5px; color: var(--ink-soft); }

  .section-title { position: absolute; display: flex; align-items: center; gap: 12px; color: var(--ink); }
  .section-title::before { content: ""; width: 22px; height: 22px; background: var(--ink); flex: none; }
  .section-title--left { font-size: 20px; font-weight: 700; }
  .section-title--right { font-size: 21px; font-weight: 700; letter-spacing: 4.5px; }
  .section-title--compact { font-size: 20px; font-weight: 700; letter-spacing: 0; }

  .personal { position: absolute; left: 73px; top: 176px; list-style: none; font-size: 16px; line-height: 25px; }
  .personal b { font-weight: 700; }

  .summary { position: absolute; left: 74px; top: 377px; width: 330px; font-size: 15px; line-height: 24.6px; }
  .summary p + p { margin-top: 24.6px; }

  .education { position: absolute; left: 468px; top: 90px; width: 340px; font-family: "Fira Sans", Arial, sans-serif; font-weight: 400; font-size: 19px; line-height: 30.5px; letter-spacing: 0.6px; color: var(--ink-soft); }
  .education p + p { margin-top: 30.5px; }

  .specialties { position: absolute; left: 474px; top: 415px; width: 320px; font-size: 16px; line-height: 28px; }

  .qualities { position: absolute; left: 460px; top: 625px; }
  .qualities text { font-family: "Lato", Arial, sans-serif; font-size: 14px; fill: var(--ink); }

  .languages { position: absolute; left: 479px; top: 958px; width: 298px; list-style: none; }
  .language { font-size: 14px; height: 56.5px; }
  .language-bar { margin-top: 5px; height: 12px; background: var(--track); }
  .language-bar span { display: block; height: 100%; background: var(--ink); }
</style>
</head>
<body>
<main class="resume">
  <aside class="sidebar"></aside>
  <div class="name-bar"></div>
  <h1 class="name">Lin-Wei Hsu</h1>
  <div class="role">ARCHITECTURE</div>

  <h2 class="section-title section-title--left" style="left:38px;top:143px;">Personal Information</h2>
  <ul class="personal">
    <li><b>Name:</b> Lin-Wei Hsu</li>
    <li><b>Date &amp; Place of birth:</b> xxxxxxx</li>
    <li><b>Nationality:</b> Taiwanese</li>
    <li><b>Address:</b> xxxxxxxx, Germany</li>
    <li><b>Mobile:</b> +xxxxxx</li>
    <li><b>Email:</b> xxxxxx@mailhub.com</li>
  </ul>

  <h2 class="section-title section-title--left" style="left:38px;top:346px;">Summary:</h2>
  <div class="summary">
    <p>Mandarin Chinese/German/English speaker, real machining experiences, OEM skills, trade skill, global sourcing. Currently, I am a “Sales manager Asia” of a top German rotary table company. I am in charge of four countries Japan, China, South Korea and Taiwan with 3 agents, more than 20 sales men team. As a director of manufacturing, I have more than 5 years professional experiences in manufacturing metal components by different CNC-machines. I am capable of coding CNC G, M-code, designing the working path of different parts and managing the whole process.</p>
    <p>I have well understanding of mechanical outsourcing ecosystem in Taiwan. With deep knowledge of outsourcing metal components to different suppliers in Taiwan.</p>
    <p>Familiar with coordinating with different industrial processes in order to build the final products. (Black oxidizing, Different anodizing, Chemical polishing, Manganese phosphate coating, Heat treatment, and Different grinding methods) Especially love to build prototype in order to get a high profitable potential products. (from zero to one)</p>
  </div>

  <h2 class="section-title section-title--right" style="left:432px;top:53px;">EDUCATION</h2>
  <div class="education">
    <p>MBA degree from MBS, Istituto Politecnico Lombardo. MBA, Istituto Politecnico Lombardo Italy 2011-2012</p>
    <p>Bachelor of Chemical engineering, Hsin-Tai Technical University 2005-2009</p>
  </div>

  <h2 class="section-title section-title--compact" style="left:438px;top:389px;">SPECIALTIES:</h2>
  <p class="specialties">Great experiences in handling business with Chinese-cultural business firms. Multi-national corporations skills (especially in Chinese-speaking market)</p>

  <h2 class="section-title section-title--right" style="left:432px;top:588px;">KEY QUALITIES</h2>
  <svg class="qualities" width="240" height="260" viewBox="0 0 240 260" role="img" aria-label="Key qualities: Specialist, Innovative, Creative, Team Work, Dependable">
    <g fill="none" stroke="#333333" stroke-width="1.3">
      <circle cx="60" cy="61" r="52"/>
      <circle cx="177" cy="61" r="52"/>
      <circle cx="119" cy="129" r="52"/>
      <circle cx="60" cy="197" r="52"/>
      <circle cx="177" cy="197" r="52"/>
    </g>
    <g text-anchor="middle">
      <text x="60" y="66">Specialist</text>
      <text x="177" y="66">Innovative</text>
      <text x="119" y="134">Creative</text>
      <text x="60" y="202">Team Work</text>
      <text x="177" y="202">Dependable</text>
    </g>
  </svg>

  <h2 class="section-title section-title--right" style="left:444px;top:918px;">LANGUAGES</h2>
  <ul class="languages">
    <li class="language">native Chinese speaker<div class="language-bar"><span style="width:217px"></span></div></li>
    <li class="language">advanced English<div class="language-bar"><span style="width:217px"></span></div></li>
    <li class="language">advanced German<div class="language-bar"><span style="width:164px"></span></div></li>
  </ul>
</main>
</body>
</html>
```